Pregnancy and Fertility Information Website

Hello Designers,
I need a website which provide tips and information about healthy and happy pregnancy. My website name is Lorvin medical.

The website should provide all the information needed throughout pregnancy and beyond ranging from pregnancy tracking tools and articles about common pregnancy concerns and what to expect during pregnancy,etc.
The details about first trimester, second trimester and third trimester should be highlighted in the website.

Top Navigation
Home, Fertility, Pregnancy basics, Articles, Tips and News

I'm looking for a simple and clean design which involves captivating images and colors but it shouldn't be crowded. The design must be professional and modern. An easy to navigate layout is a must.

Green, violet, blue and light yellow colors are my favorites but i'm open to other options.

Any questions. Kindly ask

Industry/Entity Type

Medical

```html
<!DOCTYPE html>
<html lang="en">
<head>
<meta charset="utf-8">
<title>Lorvin medical – Healthy and Happy Pregnancy</title>
<link href="https://fonts.googleapis.com/css2?family=Arimo:wght@400;700&family=Open+Sans:wght@400;600&family=Raleway:wght@300;400;500&display=swap" rel="stylesheet">
<style>
:root{
  --blue:#2f8fc7;
  --blue-dark:#1f4f99;
  --sky:#9fd4f2;
  --sky-light:#d7eefb;
  --green:#6cbf5d;
  --grey-text:#6a6a6a;
  --panel:#f6f6f6;
  --white:#ffffff;
}
*{box-sizing:border-box;margin:0;padding:0}
html,body{width:1200px;height:2209px;overflow:hidden}
body{position:relative;background:var(--white);font-family:"Arimo",Arial,sans-serif;color:var(--grey-text)}
h2,h3{font-weight:400}
.abs{position:absolute}

/* header */
.site-header{left:0;top:0;width:1200px;height:118px;background:linear-gradient(90deg,#eaf5fb 0%,#f6fbfe 45%,#dceefa 100%)}
.brand{left:92px;top:36px;display:flex;align-items:center;gap:14px}
.brand-dot{width:30px;height:30px;border-radius:50%;background:var(--green)}
.brand-name{font-family:"Open Sans",sans-serif;font-weight:600;font-size:46px;color:var(--blue);line-height:1}
.call{left:721px;top:40px;display:flex;align-items:center;gap:10px}
.call-label{font-family:"Open Sans",sans-serif;font-size:13px;color:#444;line-height:1}
.call-number{font-family:"Open Sans",sans-serif;font-size:20px;color:#444;line-height:1.1}
.social{top:45px;width:28px;height:28px;border-radius:50%;background:linear-gradient(#d9d9d9,#9e9e9e);border:2px solid #eee}

/* nav */
.main-nav{left:0;top:118px;width:1200px;height:50px;background:var(--blue)}
.main-nav a{position:absolute;top:15px;font-family:"Open Sans",sans-serif;font-size:15px;color:var(--white);text-decoration:none;letter-spacing:.2px}

/* hero */
.hero{left:0;top:168px;width:1200px;height:480px;background:linear-gradient(90deg,#cfe6f4 0%,#e9f4fa 30%,#d4ebf7 80%,#a9d3ee 100%)}
.hero-photo{left:100px;top:168px;width:580px;height:480px;background:linear-gradient(120deg,#e4e4e6 0%,#cfcdd1 45%,#b9a8a0 70%,#efeff1 100%)}
.hero-panel{left:680px;top:168px;width:418px;height:480px;background:linear-gradient(180deg,#eef7ee 0%,#e1f1e8 60%,#d6ecf3 100%)}
.hero-kicker{left:710px;top:298px;font-family:"Open Sans",sans-serif;font-size:17px;color:#111}
.hero-line1{left:708px;top:322px;font-family:"Open Sans",sans-serif;font-size:34px;color:var(--green);letter-spacing:-.5px}
.hero-line1 span{color:var(--blue)}
.hero-line2{left:707px;top:362px;font-family:"Open Sans",sans-serif;font-size:41px;color:var(--blue-dark);letter-spacing:-.5px}
.hero-text{left:711px;top:431px;width:362px;font-size:14.5px;line-height:20px;color:#777}
.hero-btn{left:711px;top:543px;width:146px;height:40px;background:var(--white);border-radius:3px;display:flex;align-items:center;padding-left:12px;gap:20px;font-family:"Open Sans",sans-serif;font-size:13px;color:#555}

/* welcome */
.welcome{left:0;top:648px;width:1200px;height:250px;background:var(--panel);text-align:center}
.welcome-title{position:absolute;left:0;width:1200px;top:24px;font-family:"Raleway",sans-serif;font-size:25px;color:#555}
.welcome-title span{color:var(--blue)}
.divider{position:absolute;left:438px;top:76px}
.welcome-text{position:absolute;left:124px;top:102px;width:952px;font-size:13.2px;line-height:22px;color:#666}
.read-more{position:absolute;left:0;width:1200px;top:200px;font-size:14px;color:#444}

/* trimesters */
.tri{top:945px;width:300px;text-align:center}
.tri-title{margin-top:131px;font-family:"Raleway",sans-serif;font-size:19px;color:#444;letter-spacing:.3px}
.tri-text{margin:10px auto 0;width:262px;font-size:12.8px;line-height:20px;color:#666}
.learn{margin-top:18px;display:flex;justify-content:center;align-items:center;gap:12px;font-size:14px;color:#333}
.learn-icon{width:20px;height:20px}

/* invest */
.invest{left:0;top:1303px;width:1200px;height:459px;background:linear-gradient(100deg,#f3eef2 0%,#e7dde0 30%,#f0eef1 55%,#d6e4ef 80%,#eef3f7 100%)}
.card-tab{height:37px;background:var(--sky-light);opacity:.95;font-family:"Open Sans",sans-serif;font-size:17px;color:#555;text-align:center;line-height:37px}
.card-body{background:var(--sky);opacity:.95}
.card-photo{width:150px;height:150px;border-radius:50%;border:3px solid var(--white);background:linear-gradient(135deg,#f2e8da,#d7b89a 60%,#c9d4dc)}
.card-text{width:200px;text-align:center;font-size:12.8px;font-weight:700;line-height:17px;color:var(--white)}
.card-btn{width:181px;height:31px;background:#f4f4f4;text-align:center;line-height:31px;font-size:13.5px;color:#666}

/* testimonial */
.testi-title{left:0;top:1806px;width:1200px;text-align:center;font-family:"Raleway",sans-serif;font-size:25px;color:#555}
.testi-title span{color:var(--blue)}
.avatar{left:577px;top:1852px;width:100px;height:100px;border-radius:50%;border:3px solid var(--blue);background:linear-gradient(135deg,#e9ddd2,#b08a6c 55%,#5a3d2c)}
.testi-text{left:150px;top:1968px;width:1012px;text-align:center;font-size:11.8px;line-height:22px;color:#333}
.testi-by{left:0;top:2054px;width:1200px;text-align:center;font-size:14px;font-style:italic;color:#222}
.testi-by span{color:var(--blue)}

/* footer */
.site-footer{left:0;top:2131px;width:1200px;height:78px;background:var(--blue);text-align:center;color:var(--white);font-size:12px}
.footer-links{position:absolute;left:0;width:1200px;top:25px}
.copyright{position:absolute;left:0;width:1200px;top:47px}
</style>
</head>
<body>

<header class="site-header abs"></header>
<div class="brand abs"><span class="brand-dot"></span><span class="brand-name">Lorvin</span></div>
<div class="call abs">
  <svg width="26" height="26" viewBox="0 0 24 24"><path fill="#555" d="M6.6 10.8a15.1 15.1 0 0 0 6.6 6.6l2.2-2.2c.3-.3.7-.4 1-.2 1.1.4 2.3.6 3.6.6.6 0 1 .4 1 1V20c0 .6-.4 1-1 1C10.6 21 3 13.4 3 4c0-.6.4-1 1-1h3.5c.6 0 1 .4 1 1 0 1.3.2 2.5.6 3.6.1.3 0 .7-.2 1z"/></svg>
  <div><div class="call-label">Call Now Today</div><div class="call-number">+1 (555) 014-2290</div></div>
</div>
<span class="social abs" style="left:969px"></span>
<span class="social abs" style="left:1005px"></span>
<span class="social abs" style="left:1040px"></span>

<nav class="main-nav abs">
  <a href="#" style="left:105px">HOME</a>
  <a href="#" style="left:186px">FERTILITY</a>
  <a href="#" style="left:302px">PRAGNANCY BASICS</a>
  <a href="#" style="left:487px">ARTICLES</a>
  <a href="#" style="left:590px">TIPS AND NEWS</a>
  <a href="#" style="left:741px">CONTACT US</a>
  <a href="#" style="left:872px">SITEMAP</a>
</nav>

<section class="hero abs"></section>
<div class="hero-photo abs" role="img" aria-label="Smiling pregnant woman resting on white pillows"></div>
<div class="hero-panel abs"></div>
<div class="hero-kicker abs">WE PROVIDE INFORMATION ABOUT</div>
<div class="hero-line1 abs">ABOUT HEALTHY <span>AND</span></div>
<div class="hero-line2 abs">HAPPY PREGNANCY</div>
<p class="hero-text abs">simply dummy text of the printing and typesetting industry. Lorem Ipsum has been the industry's standard dummy text ever since the 1500s, when an unknown printer took a galley of type and scrambled it to make a type specimen book.</p>
<div class="hero-btn abs">READ MORE
  <svg width="20" height="20" viewBox="0 0 20 20"><circle cx="10" cy="10" r="10" fill="#2f8fc7"/><path d="M8 6l4 4-4 4" stroke="#fff" stroke-width="2" fill="none"/></svg>
</div>

<section class="welcome abs">
  <h2 class="welcome-title">Welcome to <span>Lorvin Pragnancy</span> health care</h2>
  <svg class="divider" width="324" height="10" viewBox="0 0 324 10"><line x1="0" y1="5" x2="155" y2="5" stroke="#ccc"/><circle cx="162" cy="5" r="4" fill="none" stroke="#2f8fc7" stroke-width="1.5"/><line x1="169" y1="5" x2="324" y2="5" stroke="#ccc"/></svg>
  <p class="welcome-text">simply dummy text of the printing and typesetting industry. Lorem Ipsum has been the industry's standard dummy text ever since the 1500s, when an unknown printer took a galley of type and scrambled it to make a type specimen book. It has survived not only five centuries but also the leap into electronic typesetting, remaining essentially unchanged. It was popularised in the 1960s with the release of Tessaline sheets containing Lorem Ipsum passages, and more recently with desktop publishing software like Quillbright Layout including versions of Lorem Ipsum.</p>
  <div class="read-more">Read More ››</div>
</section>

<div class="tri abs" style="left:100px">
  <svg class="abs" style="left:94px;top:0" width="112" height="112" viewBox="0 0 112 112"><path d="M6 56a50 50 0 0 1 100 0" fill="none" stroke="#c9c9c9" stroke-width="8"/><path d="M106 56a50 50 0 0 1-100 0" fill="none" stroke="#6cbf5d" stroke-width="8"/><path d="M36 42h26a6 6 0 0 1 6 6v10a6 6 0 0 1-6 6H46l-8 6v-6h-2a6 6 0 0 1-6-6V48a6 6 0 0 1 6-6z" fill="none" stroke="#6cbf5d" stroke-width="2.5"/><rect x="52" y="54" width="28" height="18" rx="7" fill="#6cbf5d"/><circle cx="59" cy="63" r="2" fill="#fff"/><circle cx="66" cy="63" r="2" fill="#fff"/><circle cx="73" cy="63" r="2" fill="#fff"/></svg>
  <h3 class="tri-title">FIRST TRIMESTER</h3>
  <p class="tri-text">Lorem Ipsum is simply dummy text of the printing and typesetting industry. Lorem Ipsum has been the industry's standard dummy text ever since the 1500s, when an</p>
  <div class="learn">Learn More <svg class="learn-icon" viewBox="0 0 20 20"><rect width="20" height="20" fill="#6cbf5d"/><path d="M8 5l5 5-5 5" stroke="#fff" stroke-width="2" fill="none"/></svg></div>
</div>
<div class="tri abs" style="left:439px">
  <svg class="abs" style="left:94px;top:0" width="112" height="112" viewBox="0 0 112 112"><path d="M6 56a50 50 0 0 1 100 0" fill="none" stroke="#c9c9c9" stroke-width="8"/><path d="M106 56a50 50 0 0 1-100 0" fill="none" stroke="#6cbf5d" stroke-width="8"/><path d="M36 42h26a6 6 0 0 1 6 6v10a6 6 0 0 1-6 6H46l-8 6v-6h-2a6 6 0 0 1-6-6V48a6 6 0 0 1 6-6z" fill="none" stroke="#6cbf5d" stroke-width="2.5"/><rect x="52" y="54" width="28" height="18" rx="7" fill="#6cbf5d"/><circle cx="59" cy="63" r="2" fill="#fff"/><circle cx="66" cy="63" r="2" fill="#fff"/><circle cx="73" cy="63" r="2" fill="#fff"/></svg>
  <h3 class="tri-title">SECOND TRIMESTER</h3>
  <p class="tri-text">Lorem Ipsum is simply dummy text of the printing and typesetting industry. Lorem Ipsum has been the industry's standard dummy text ever since the 1500s, when an</p>
  <div class="learn">Learn More <svg class="learn-icon" viewBox="0 0 20 20"><rect width="20" height="20" fill="#6cbf5d"/><path d="M8 5l5 5-5 5" stroke="#fff" stroke-width="2" fill="none"/></svg></div>
</div>
<div class="tri abs" style="left:772px">
  <svg class="abs" style="left:94px;top:0" width="112" height="112" viewBox="0 0 112 112"><path d="M6 56a50 50 0 0 1 100 0" fill="none" stroke="#c9c9c9" stroke-width="8"/><path d="M106 56a50 50 0 0 1-100 0" fill="none" stroke="#6cbf5d" stroke-width="8"/><path d="M36 42h26a6 6 0 0 1 6 6v10a6 6 0 0 1-6 6H46l-8 6v-6h-2a6 6 0 0 1-6-6V48a6 6 0 0 1 6-6z" fill="none" stroke="#6cbf5d" stroke-width="2.5"/><rect x="52" y="54" width="28" height="18" rx="7" fill="#6cbf5d"/><circle cx="59" cy="63" r="2" fill="#fff"/><circle cx="66" cy="63" r="2" fill="#fff"/><circle cx="73" cy="63" r="2" fill="#fff"/></svg>
  <h3 class="tri-title">THIRD TRIMESTER</h3>
  <p class="tri-text">Lorem Ipsum is simply dummy text of the printing and typesetting industry. Lorem Ipsum has been the industry's standard dummy text ever since the 1500s, when an</p>
  <div class="learn">Learn More <svg class="learn-icon" viewBox="0 0 20 20"><rect width="20" height="20" fill="#6cbf5d"/><path d="M8 5l5 5-5 5" stroke="#fff" stroke-width="2" fill="none"/></svg></div>
</div>

<section class="invest abs" role="img" aria-label="Soft blurred photo of a mother resting"></section>

<div class="card-tab abs" style="left:184px;top:1374px;width:247px">INVEST HEALTHY YOU</div>
<div class="card-body abs" style="left:184px;top:1411px;width:247px;height:294px"></div>
<div class="card-photo abs" style="left:224px;top:1425px" role="img" aria-label="Pregnant woman eating a salad"></div>
<p class="card-text abs" style="left:207px;top:1591px">Lorem Ipsum is simply dummy text of the printing and typeset-ting industry.</p>
<div class="card-btn abs" style="left:208px;top:1651px">Read more ››</div>

<div class="card-tab abs" style="left:487px;top:1374px;width:248px">INVEST HEALTHY YOU</div>
<div class="card-body abs" style="left:487px;top:1411px;width:248px;height:294px"></div>
<div class="card-photo abs" style="left:528px;top:1425px" role="img" aria-label="Woman talking on the phone"></div>
<p class="card-text abs" style="left:511px;top:1591px">Lorem Ipsum is simply dummy text of the printing and typeset-ting industry.</p>
<div class="card-btn abs" style="left:515px;top:1651px">Read more ››</div>

<div class="card-tab abs" style="left:794px;top:1370px;width:247px">INVEST HEALTHY YOU</div>
<div class="card-body abs" style="left:794px;top:1407px;width:247px;height:294px"></div>
<div class="card-photo abs" style="left:832px;top:1421px" role="img" aria-label="Pregnant woman measuring her belly"></div>
<p class="card-text abs" style="left:817px;top:1588px">Lorem Ipsum is simply dummy text of the printing and typeset-ting industry.</p>
<div class="card-btn abs" style="left:823px;top:1651px">Read more ››</div>

<h2 class="testi-title abs"><span>Client's</span> Testimonial</h2>
<div class="avatar abs" role="img" aria-label="Portrait of a client"></div>
<p class="testi-text abs">simply dummy text of the printing and typesetting industry. Lorem Ipsum has been the industry's standard dummy text ever since the 1500s, when an unknown printer took a galley of type and scrambled it to make a type specimen book. It has survived not only five centuries, but also the leap into electronic typesetting, remaining essentially unchanged. It was popularised in the 1960s with the release of Tessaline sheets containing Lorem Ipsum passages, and more recently with desktop</p>
<p class="testi-by abs">By <span>Admin</span></p>

<footer class="site-footer abs">
  <div class="footer-links">Home &nbsp;|&nbsp; Fertility &nbsp;|&nbsp; Pragnancy Basics &nbsp;|&nbsp; Articles &nbsp;|&nbsp; Tips and News &nbsp;|&nbsp; Contact Us &nbsp;|&nbsp; Testimonials</div>
  <div class="copyright">Copyright 2017 | Lorvin</div>
</footer>

</body>
</html>
```